Business Card Design

An energy company designed around renewable energy and energy storage that focuses on providing its energy at points on the grid that reduce costs and add value to the system.

Industry/Entity Type

Business

Contact Information for Business Card

Martin Delacroix
Executive Vice President
41 K ST NE
Washington, DC 20017
240-555-0183
mdelacroix@harborvoltco.example

```html
<!DOCTYPE html>
<html lang="en">
<head>
<meta charset="utf-8">
<title>Harbor Volt — Business Card</title>
<link rel="stylesheet" href="https://fonts.googleapis.com/css2?family=Didact+Gothic&display=swap">
<style>
  :root {
    --backdrop: #2a2a2a;
    --card-dark: #1b1b1b;
    --card-mid: #343434;
    --green: #6ab43e;
    --green-deep: #4f8f2c;
    --white: #f2f2f2;
    --grey-text: #d9d9d9;
  }
  * { margin: 0; padding: 0; box-sizing: border-box; }
  html, body {
    width: 1200px; height: 800px; overflow: hidden;
    background: var(--backdrop);
    font-family: "Didact Gothic", "Century Gothic", sans-serif;
  }
  .business-card {
    position: absolute; left: 75px; top: 100px;
    width: 1050px; height: 600px;
    background: var(--card-dark);
    overflow: hidden;
    box-shadow: 0 14px 40px rgba(0,0,0,.55);
  }
  .card-texture {
    position: absolute; inset: 0;
    background: radial-gradient(ellipse at 45% 55%, var(--card-mid) 0%, var(--card-dark) 75%);
  }
  .brand {
    position: absolute; left: 70px; top: 140px;
    display: flex; align-items: center; gap: 18px;
  }
  .brand-dot {
    width: 40px; height: 40px; border-radius: 50%;
    background: var(--green);
  }
  .brand-name {
    font-size: 76px; color: var(--green); letter-spacing: 2px; line-height: 1;
  }
  .holder {
    position: absolute; right: 70px; top: 50px; text-align: right;
  }
  .holder-name { font-size: 40px; font-weight: 400; color: var(--white); letter-spacing: 1.5px; }
  .holder-title { font-size: 24px; color: var(--green); letter-spacing: 1px; margin-top: 4px; }
  .contact-list {
    position: absolute; right: 60px; top: 255px;
    list-style: none; text-align: right;
  }
  .contact-item {
    display: flex; justify-content: flex-end; align-items: center; gap: 18px;
    font-size: 27px; color: var(--grey-text); letter-spacing: 1.5px;
    height: 58px;
  }
  .contact-icon { width: 44px; height: 44px; flex: none; }
  .accent-band {
    position: absolute; left: 0; bottom: 0; width: 100%; height: 58px;
    background: var(--green);
    border-top: 3px solid var(--green-deep);
  }
</style>
</head>
<body>
  <main class="business-card">
    <div class="card-texture" role="img" aria-label="Soft dark background with a subtle curved light pattern"></div>

    <div class="brand">
      <span class="brand-dot"></span>
      <span class="brand-name">Harbor Volt</span>
    </div>

    <header class="holder">
      <h1 class="holder-name">Martin Delacroix</h1>
      <p class="holder-title">Executive Vice President</p>
    </header>

    <ul class="contact-list">
      <li class="contact-item">
        <span>240-555-0183</span>
        <svg class="contact-icon" viewBox="0 0 44 44" aria-hidden="true">
          <polygon points="22,2 40,12 40,32 22,42 4,32 4,12" fill="#6ab43e"/>
          <path d="M15 13 l4 -1 l3 6 l-2.5 2 a12 12 0 0 0 5 5 l2 -2.5 l6 3 l-1 4 c-9 1 -18 -8 -16.5 -16.5 z" fill="#fff"/>
        </svg>
      </li>
      <li class="contact-item">
        <span>mdelacroix@harborvoltco.example</span>
        <svg class="contact-icon" viewBox="0 0 44 44" aria-hidden="true">
          <polygon points="22,2 40,12 40,32 22,42 4,32 4,12" fill="#6ab43e"/>
          <rect x="11" y="14" width="22" height="16" fill="none" stroke="#fff" stroke-width="2"/>
          <path d="M11 14 L22 23 L33 14" fill="none" stroke="#fff" stroke-width="2"/>
        </svg>
      </li>
      <li class="contact-item">
        <span>41 K ST NE &nbsp;Washington, DC 20017</span>
        <svg class="contact-icon" viewBox="0 0 44 44" aria-hidden="true">
          <polygon points="22,2 40,12 40,32 22,42 4,32 4,12" fill="#6ab43e"/>
          <path d="M22 33 C 15 24, 14 21, 14 18 a8 8 0 0 1 16 0 c0 3 -1 6 -8 15 z" fill="#fff"/>
          <circle cx="22" cy="18" r="3" fill="#6ab43e"/>
        </svg>
      </li>
    </ul>

    <div class="accent-band"></div>
  </main>
</body>
</html>
```